Innovative Fashion Business needs Branding and Business Card.

We need a Business Card and Branding work (Email Footer, Stickers, letterhead, all from same Design) We are an innovative, progressive and exciting Fashion Start-up. We are called "Moss Tide" I am attaching the original artwork of the image I want to use. Also have a previous Card, I want to do something like that, only using this new image.

```html
<!DOCTYPE html>
<html lang="en">
<head>
<meta charset="utf-8">
<title>Moss Tide – Business Card</title>
<link href="https://fonts.googleapis.com/css2?family=Exo+2:wght@500;600&family=Montserrat:wght@400;500&display=swap" rel="stylesheet">
<style>
  :root {
    --backdrop: #7a3470;
    --card: #ffffff;
    --ink: #3e0d38;
    --brand: #7b2d7a;
    --frame-light: #f3eef3;
    --frame-mid: #d9cddc;
    --art-lilac: #c9a6cf;
    --art-rose: #e8c3cf;
    --art-plum: #8c4a8a;
  }
  * { box-sizing: border-box; margin: 0; padding: 0; }
  html, body { width: 1200px; height: 900px; overflow: hidden; }
  body {
    background: var(--backdrop);
    position: relative;
    font-family: "Exo 2", sans-serif;
  }
  .card {
    position: absolute;
    left: 280px;
    width: 640px;
    height: 366px;
    background: var(--card);
    border-radius: 3px;
    box-shadow: 0 8px 24px rgba(40, 0, 35, 0.35);
    overflow: hidden;
  }
  .card-back { top: 60px; }
  .card-front { top: 474px; }

  /* Contact side */
  .contact {
    height: 100%;
    display: flex;
    flex-direction: column;
    align-items: center;
    justify-content: center;
    color: var(--ink);
    text-align: center;
  }
  .contact-name { font-size: 36px; font-weight: 600; letter-spacing: 0.5px; line-height: 1.1; }
  .contact-role { font-size: 18px; font-weight: 500; margin-top: 2px; }
  .contact-services { font-size: 19px; font-weight: 500; margin-top: 18px; line-height: 1.3; letter-spacing: 0.3px; }
  .contact-details { font-size: 20px; font-weight: 500; margin-top: 18px; line-height: 1.35; letter-spacing: 0.4px; }

  /* Brand side */
  .front-frame {
    position: absolute;
    inset: 0;
    background: radial-gradient(ellipse at 50% 95%, var(--art-lilac) 0%, var(--frame-mid) 30%, var(--frame-light) 65%);
  }
  .front-panel {
    position: absolute;
    left: 56px; right: 56px; top: 30px; bottom: 52px;
    background: var(--card);
    display: flex;
    flex-direction: column;
    align-items: center;
    padding-top: 22px;
    font-family: "Montserrat", sans-serif;
  }
  .brand-name {
    font-size: 46px;
    font-weight: 500;
    color: var(--brand);
    letter-spacing: 1px;
    line-height: 1;
    text-transform: uppercase;
  }
  .brand-art {
    width: 300px;
    height: 160px;
    margin-top: 12px;
    background: linear-gradient(135deg, var(--frame-light) 0%, var(--art-rose) 45%, var(--art-lilac) 75%, var(--art-plum) 100%);
  }
  .brand-tagline {
    font-size: 17px;
    color: var(--ink);
    margin-top: 14px;
    letter-spacing: 0.3px;
  }
</style>
</head>
<body>
  <section class="card card-back">
    <div class="contact">
      <h1 class="contact-name">Hero Love</h1>
      <p class="contact-role">Partner &amp; Strategist</p>
      <p class="contact-services">Boutique development &amp; sourcing<br>Sustainability &amp; Innovation</p>
      <p class="contact-details">+852 5550 3147<br>Hero@mosstide.asia<br>www.mosstide.asia</p>
    </div>
  </section>

  <section class="card card-front">
    <div class="front-frame" role="img" aria-label="Hand-drawn border of flowers, hearts, swirls and stars in grey and lilac"></div>
    <div class="front-panel">
      <h2 class="brand-name">Moss Tide</h2>
      <div class="brand-art" role="img" aria-label="Ink illustration of a couple with a small dog, hearts and a flower in pink and purple tones"></div>
      <p class="brand-tagline">Purveyoors pf Inspiration &amp; Opportunity</p>
    </div>
  </section>
</body>
</html>
```